Birchfield Dental Care Stationery

create stationery, business cards and envelops for business. Use current logo on website but open to new fonts for the business name. Business name is Birchfield Dental Care, would like below the name added "Cosmetic - Family - Implants" Website is www.birchfielddentalcareQX.example. I would like to have modern look, clean, and professional. The water mark of the logo is a great thing to ad as well.

Target Market(s)

General public, Families, Cosmetic, Implant

Industry/Entity Type

Dental

Font styles to use
Sans Serif

Colors
9bcb3c
000000
757575
c9c9c9

Requirements
Must have
• Would like to see different versions of the current logo. Improvements, color, sytle, and class.
Nice to have
• current font has double "oo" in the Birchfield logo, does not need to have with new logo.

```html
<!DOCTYPE html>
<html lang="en">
<head>
<meta charset="utf-8">
<title>Birchfield Dental Care Letterhead</title>
<link href="https://fonts.googleapis.com/css2?family=PT+Sans+Narrow:wght@400;700&display=swap" rel="stylesheet">
<style>
  :root {
    --green: #9bcb3c;
    --green-deep: #2f9a3c;
    --ink: #000000;
    --grey: #757575;
    --silver: #c9c9c9;
    --paper: #ffffff;
    --backdrop: #93d8ac;
    --wash: #f3f6f4;
    --watermark: #e9efdf;
  }
  html, body {
    margin: 0; padding: 0;
    width: 1200px; height: 784px;
    overflow: hidden;
    background: var(--backdrop);
    font-family: "PT Sans Narrow", sans-serif;
  }
  .letterhead {
    position: absolute;
    left: 314px; top: 22px;
    width: 572px; height: 740px;
    background: var(--paper);
    box-shadow: 0 6px 18px rgba(0,0,0,0.12);
    overflow: hidden;
  }
  .decor { position: absolute; inset: 0; pointer-events: none; }
  .edge-band {
    position: absolute; left: 0; top: 235px; bottom: 0;
    width: 7px; background: var(--green-deep);
  }
  .brand {
    position: absolute; top: 24px; right: 30px;
    display: flex; align-items: center; gap: 10px;
  }
  .brand-dot {
    width: 34px; height: 34px; border-radius: 50%;
    background: var(--green);
  }
  .brand-name {
    font-weight: 700; font-size: 22px; line-height: 1;
    color: var(--green-deep); letter-spacing: 0.3px;
  }
  .brand-tagline {
    font-size: 10px; color: var(--green-deep); margin-top: 3px;
    letter-spacing: 0.4px;
  }
  .info-row {
    position: absolute; left: 24px; right: 24px; top: 78px;
    display: flex; gap: 18px; justify-content: flex-end;
  }
  .info-block { font-size: 7.5px; line-height: 10px; color: var(--green-deep); }
  .info-label {
    display: inline-block; background: var(--green);
    color: var(--paper); font-weight: 700; font-size: 9px;
    padding: 1px 8px; margin-bottom: 4px;
  }
  .info-block ul { list-style: none; margin: 0; padding: 0; }
  .services ul { columns: 2; column-gap: 14px; }
  .services li::before {
    content: ""; display: inline-block; width: 0; height: 0;
    border-left: 4px solid var(--green-deep);
    border-top: 2.5px solid transparent; border-bottom: 2.5px solid transparent;
    margin-right: 3px;
  }
  .divider {
    position: absolute; left: 0; right: 40px; top: 235px;
    height: 1px; background: var(--green-deep);
  }
  .watermark {
    position: absolute; left: 150px; top: 360px;
    display: flex; align-items: center; gap: 14px;
    pointer-events: none;
  }
  .watermark-circle {
    width: 110px; height: 110px; border-radius: 50%;
    background: var(--watermark);
  }
  .watermark-name {
    font-weight: 700; font-size: 30px; line-height: 1;
    color: var(--watermark);
  }
</style>
</head>
<body>
<main class="letterhead">
  <svg class="decor" width="572" height="740" viewBox="0 0 572 740" aria-hidden="true">
    <defs>
      <linearGradient id="footWash" x1="0" y1="0" x2="0" y2="1">
        <stop offset="0" stop-color="#ffffff" stop-opacity="0"/>
        <stop offset="1" stop-color="#eef3f0"/>
      </linearGradient>
    </defs>
    <path d="M7 250 C 90 300, 170 330, 300 420" fill="none" stroke="#f1f3f1" stroke-width="10" stroke-linecap="round"/>
    <path d="M7 285 C 80 330, 140 360, 250 450" fill="none" stroke="#f4f5f4" stroke-width="5" stroke-linecap="round"/>
    <path d="M7 560 C 160 520, 360 560, 572 470 L572 740 L7 740 Z" fill="url(#footWash)"/>
  </svg>
  <div class="edge-band"></div>

  <header class="brand">
    <span class="brand-dot"></span>
    <div class="brand-text">
      <div class="brand-name">Birchfield Dental Care</div>
      <div class="brand-tagline">Cosmetic • Family • Implants</div>
    </div>
  </header>

  <section class="info-row">
    <div class="info-block contact">
      <span class="info-label">Contact:</span>
      <ul>
        <li>Dentist Maple Hollow, QX</li>
        <li>Alan Mercer D.D.S.</li>
        <li>Birchfield Dental Health Center</li>
        <li>1280 North Alder Lane</li>
        <li>Maple Hollow, QX 00412</li>
        <li>(555) 014-2290 Ph</li>
        <li>(555) 014-2291 Fax</li>
        <li>www.birchfielddentalcareQX.example</li>
      </ul>
    </div>
    <div class="info-block hours">
      <span class="info-label">Office Hours</span>
      <ul>
        <li>Monday 08:00 AM - 05:00 PM</li>
        <li>Tuesday 08:00 AM - 06:00 PM</li>
        <li>Wednesday By Appointment Only</li>
        <li>Thursday 08:00 AM - 06:00 PM</li>
        <li>Friday 08:00 AM - 03:00 PM</li>
        <li>Saturday Available by appointment</li>
        <li>Sunday Closed</li>
      </ul>
    </div>
    <div class="info-block services">
      <span class="info-label">Services:</span>
      <ul>
        <li>Bonding</li>
        <li>Cosmetic Contouring</li>
        <li>Crowns and Bridges</li>
        <li>Specialty Dentures</li>
        <li>Cosmetic Fillings</li>
        <li>Implants</li>
        <li>Veneers</li>
        <li>Teeth Whitening</li>
        <li>Bone Grafting</li>
        <li>Excessive or Uneven Gums</li>
        <li>Inlays and Onlays</li>
        <li>TMJ</li>
        <li>Nitrous Oxide Sedation</li>
        <li>Oral Sedation</li>
        <li>Sealants</li>
        <li>Root Canal Therapy</li>
        <li>Extractions</li>
        <li>Scaling and Root Planing</li>
        <li>Implant Retained Dentures</li>
        <li>Cosmetic Dentistry</li>
        <li>Sleep Apnea Treatment</li>
        <li>Snoring Treatment</li>
        <li>Maxillofacial Surgery</li>
        <li>Laser Dentistry</li>
        <li>Laser Surgery</li>
        <li>Dental Emergencies</li>
      </ul>
    </div>
  </section>

  <div class="divider"></div>

  <div class="watermark" aria-hidden="true">
    <span class="watermark-circle"></span>
    <span class="watermark-name">Birchfield Dental Care</span>
  </div>
</main>
</body>
</html>
```